Design an Advertisement for Email Marketing

We provide Email Marketing Service.
We Send Email Campaigns on behalf of our Clients
Our Database size is 100,000 Contact in Dubai
After Email Campaign sent a report will be provided to customer: Open Rate, Click Through Rate...etc.
We want this message to reach our target customers by email.
Prices are:
1 Email Campaign 499 AED (UAE Dirhams)
3 Email Campaign 1422 AED
6 Email Campaign 2695 AED
12 Email Campaign 5089 AED
24 Email Campaign 9580 AED

Pay online and save 5% Extra

The design Should have button to take action (Buy now) - Monexa Button
I will slice the design later and link each package with payment
PSD File must be provided afterwards

Please allow prices to be edited from time to time
Call now for more information: +971 52 xxx xxxx or email: info@fanoosmedia.example

File to submit : ONLY PSD
Our LOGO is (AL Fanoos) - Need simple logo here
Good luck

```html
<!DOCTYPE html>
<html lang="en">
<head>
<meta charset="utf-8">
<title>AL Fanoos – Email Marketing Offer</title>
<link rel="stylesheet" href="https://fonts.googleapis.com/css2?family=Arimo:ital,wght@0,400;0,700;1,700&family=Tinos:wght@400;700&display=swap">
<style>
  :root {
    --navy: #0a2f66;
    --deep: #06204a;
    --blue: #1565b8;
    --text-blue: #14518f;
    --accent-red: #e0141e;
    --panel: rgba(214, 236, 252, 0.88);
    --gold-light: #f7dd5a;
    --gold: #e2b41c;
    --gold-dark: #5a3a08;
    --white: #ffffff;
    --black: #0b0b0b;
    --rule: #c9d9ea;
  }
  * { box-sizing: border-box; margin: 0; padding: 0; }
  html, body { width: 900px; height: 1200px; overflow: hidden; background: var(--white); }
  .ad {
    position: relative;
    width: 900px;
    height: 1200px;
    overflow: hidden;
    font-family: "Arimo", Arial, sans-serif;
    background: var(--white);
  }
  .backdrop { position: absolute; inset: 0; }

  .brand {
    position: absolute; left: 50px; top: 32px;
    display: flex; align-items: center; gap: 10px;
    color: var(--accent-red);
    font-weight: 700; font-size: 40px; letter-spacing: 0.5px;
  }
  .brand-dot { width: 16px; height: 16px; border-radius: 50%; background: var(--accent-red); }

  .offer-ribbon {
    position: absolute; right: 16px; top: 0;
    width: 150px; height: 250px;
  }
  .offer-text {
    position: absolute; right: 20px; top: 10px; width: 145px;
    text-align: center;
    font-family: "Tinos", "Times New Roman", serif;
    color: var(--gold-dark);
    line-height: 1.05;
  }
  .offer-text .lead { font-size: 40px; }
  .offer-text .mid { font-size: 24px; }
  .offer-text .big { font-size: 56px; }

  .skyline {
    position: absolute; left: 0; top: 0; width: 900px; height: 1200px; pointer-events: none;
  }

  .service-panel {
    position: absolute; left: 322px; top: 196px; width: 578px; height: 254px;
    background: var(--panel);
    padding: 32px 24px 0 28px;
  }
  .service-list { list-style: none; color: var(--text-blue); font-size: 19.5px; line-height: 28px; }
  .service-list li { padding-left: 22px; text-indent: -22px; }
  .service-list li::before { content: "- "; }
  .highlight { color: var(--accent-red); }
  .highlight.large { font-size: 23px; }

  .pricing {
    position: absolute; left: 495px; top: 752px; width: 350px;
    color: var(--text-blue);
  }
  .pricing-title {
    text-align: center; font-weight: 700; font-size: 21px; margin: 0 0 8px 28px;
  }
  .price-row {
    display: flex; align-items: baseline; height: 40.5px;
    font-size: 24px; border-bottom: 1px solid var(--rule);
    padding-top: 6px;
  }
  .price-row:last-child { border-bottom: 2px solid var(--rule); }
  .qty { width: 30px; text-align: right; font-weight: 700; margin-right: 12px; }
  .label { margin-right: 8px; }
  .amount { font-weight: 700; }
  .unit { margin-left: 5px; }

  .buy-now {
    position: absolute; left: 596px; top: 1004px; width: 158px; height: 38px;
    border-radius: 19px;
    background: linear-gradient(#fff3a8, var(--gold-light) 45%, var(--gold));
    border: 1px solid #c98f10;
    color: var(--navy); font-weight: 700; font-style: italic; font-size: 21px;
    display: flex; align-items: center; justify-content: center;
    text-decoration: none;
  }
  .payment-methods {
    position: absolute; left: 596px; top: 1052px; display: flex; gap: 5px;
  }
  .payment-methods span {
    width: 28px; height: 21px; border: 1px solid #9aa9b8; border-radius: 2px;
    background: linear-gradient(#ffffff, #dfe6ee);
  }

  .contact {
    position: absolute; left: 30px; top: 1074px;
    color: var(--white); font-size: 22px; line-height: 34px;
  }
  .contact strong { font-weight: 700; }

  .unsubscribe-bar {
    position: absolute; left: 0; top: 1148px; width: 900px; height: 52px;
    background: var(--black); color: var(--white);
    display: flex; align-items: center; justify-content: center;
    font-size: 25px;
  }
  .unsubscribe-bar a { color: var(--white); }
</style>
</head>
<body>
<main class="ad">
  <svg class="backdrop" viewBox="0 0 900 1200" width="900" height="1200" aria-hidden="true">
    <defs>
      <linearGradient id="footerFill" x1="0" y1="0" x2="0" y2="1">
        <stop offset="0" stop-color="#1c6fc0"/>
        <stop offset="0.5" stop-color="#0a3a80"/>
        <stop offset="1" stop-color="#061c44"/>
      </linearGradient>
      <linearGradient id="headerFill" x1="0" y1="0" x2="1" y2="0">
        <stop offset="0" stop-color="#0a2f66"/>
        <stop offset="1" stop-color="#1a6cc0"/>
      </linearGradient>
    </defs>
    <path d="M0,1062 C260,1020 560,1120 900,1040 L900,1148 L0,1148 Z" fill="url(#footerFill)"/>
    <path d="M0,1075 C260,1035 560,1135 900,1055" fill="none" stroke="#5fb2f0" stroke-width="2" opacity="0.7"/>
  </svg>

  <svg class="skyline" viewBox="0 0 900 1200" width="900" height="1200">
    <defs>
      <linearGradient id="cityFill" x1="0" y1="0" x2="0" y2="1">
        <stop offset="0" stop-color="#0b2a5e"/>
        <stop offset="0.45" stop-color="#174f8f"/>
        <stop offset="0.75" stop-color="#8fb3cf"/>
        <stop offset="1" stop-color="#e0c48a"/>
      </linearGradient>
      <linearGradient id="arrowsFill" x1="0" y1="1" x2="1" y2="0">
        <stop offset="0" stop-color="#f47ac6"/>
        <stop offset="0.35" stop-color="#a7e05a"/>
        <stop offset="0.7" stop-color="#5fc4f0"/>
        <stop offset="1" stop-color="#ffffff" stop-opacity="0"/>
      </linearGradient>
      <radialGradient id="iconFill">
        <stop offset="0" stop-color="#ffffff"/>
        <stop offset="0.7" stop-color="#bfe1fa"/>
        <stop offset="1" stop-color="#2f8fdb"/>
      </radialGradient>
      <linearGradient id="ribbonFill" x1="0" y1="0" x2="1" y2="0">
        <stop offset="0" stop-color="#c99812"/>
        <stop offset="0.45" stop-color="#f9e26a"/>
        <stop offset="1" stop-color="#d9a91a"/>
      </linearGradient>
    </defs>
    <path role="img" aria-label="Night skyline of Dubai with illuminated towers and city lights"
          d="M0,150 C300,80 600,150 900,100 L900,720 C700,760 460,650 0,602 Z" fill="url(#cityFill)"/>
    <path d="M0,112 C300,40 600,125 900,62 L900,104 C600,160 300,84 0,156 Z" fill="url(#headerFill)"/>
    <path d="M0,600 C460,648 700,758 900,718" fill="none" stroke="#2a80d0" stroke-width="6"/>
    <path role="img" aria-label="Colourful upward arrows rising diagonally"
          d="M0,700 L420,660 L470,900 L300,1040 L0,1040 Z" fill="url(#arrowsFill)" opacity="0.85"/>
    <ellipse role="img" aria-label="Email envelope icon with at sign and circular arrow"
             cx="395" cy="655" rx="88" ry="86" fill="url(#iconFill)"/>
    <path d="M735,0 H885 V205 L862,238 L838,210 L792,234 Q748,140 735,0 Z" fill="url(#ribbonFill)"/>
  </svg>

  <div class="brand"><span class="brand-dot"></span>AL Fanoos</div>

  <div class="offer-text">
    <div class="lead">Pay</div>
    <div class="mid">Online</div>
    <div class="mid">and Save</div>
    <div class="big">5%</div>
  </div>

  <section class="service-panel">
    <ul class="service-list">
      <li>We provide <span class="highlight">Email Marketing Service</span></li>
      <li>We Send Email Campaigns on behalf of our Clients</li>
      <li>Our Database size is <span class="highlight large">100,000 Contact in Dubai</span></li>
      <li>After Email Campaign sent a report will be provided to customer: Open Rate, Click Through Rate... etc.</li>
      <li>We want this message to reach our target customers by email.</li>
    </ul>
  </section>

  <section class="pricing">
    <h2 class="pricing-title">AED (UAE Dirhams)</h2>
    <div class="price-row"><span class="qty">1</span><span class="label">Email Campaign</span>&nbsp;&nbsp;<span class="amount">499</span><span class="unit">AED</span></div>
    <div class="price-row"><span class="qty">3</span><span class="label">Email Campaign</span><span class="amount">1422</span><span class="unit">AED</span></div>
    <div class="price-row"><span class="qty">6</span><span class="label">Email Campaign</span><span class="amount">2695</span><span class="unit">AED</span></div>
    <div class="price-row"><span class="qty">12</span><span class="label">Email Campaign</span><span class="amount">5089</span><span class="unit">AED</span></div>
    <div class="price-row"><span class="qty">24</span><span class="label">Email Campaign</span><span class="amount">9580</span><span class="unit">AED</span></div>
  </section>

  <a class="buy-now" href="#">Buy Now</a>
  <div class="payment-methods" aria-label="Accepted payment methods">
    <span></span><span></span><span></span><span></span><span></span>
  </div>

  <div class="contact">
    <div>Call now for <strong>more information:</strong></div>
    <div>+971 52 xxx xxxx or <strong>email:</strong> info@fanoosmedia.example</div>
  </div>

  <footer class="unsubscribe-bar">
    <span>To <strong>unsuscribe</strong>, please <a href="#">click here</a></span>
  </footer>
</main>
</body>
</html>
```